Design 2015 Winter themed holiday card

We need a holiday card for our company.

The attached brief provides all the information for the design. We provided two images for the cover or if you have something better.

CARD DESIGN 4" x 6" Vertical Folded Card
Bleed: The extra .0625" on each side of your artwork that bleeds off the edge of the piece and ensures your piece will not end up with white borders.
Trim: The final size the printed piece will be.
Safe: The .0625" area from the final trim size. Do not place text or important imagery beyond the safe line to avoid it getting cut off when the finished piece is trimmed to final size.
Corner Rounding, where available, can be 1/8" or 5/16". Examples are provided in the image below.
1/8" is a "tighter" or "smaller" corner radius.
5/16" is a "wider" or "larger" corner radius.

Target Market(s)

Government agencies, businesses and nonprofits

Industry/Entity Type

It Company

Font styles to use
Serif
Sans Serif

Requirements
Must have
• Please follow the design brief: QKRP-Strategy-Brief-Holiday-Card-11042015.pdf
• It includes the fonts, colors, design parameters - please review it before designing. I've included two previous holiday cards for your review.
• Please add "Seasons Greetings" on the cover.

```html
<!DOCTYPE html>
<html lang="en">
<head>
<meta charset="utf-8">
<title>QKRP Holiday Card</title>
<link rel="stylesheet" href="https://fonts.googleapis.com/css2?family=Crimson+Text:ital,wght@0,400;0,600;1,400&display=swap">
<style>
  :root {
    --paper: #ffffff;
    --ink: #1a1a1a;
    --brand-blue: #3d8ee6;
    --quote-blue: #4a90e2;
    --bleed-line: #e58ad0;
    --trim-line: #b9bcc0;
    --forest-dark: #3f4347;
    --forest-mid: #7d858c;
    --snow-shade: #c9d2da;
    --snow: #f3f6f9;
  }
  * { box-sizing: border-box; margin: 0; padding: 0; }
  html, body {
    width: 1200px;
    height: 911px;
    overflow: hidden;
    background: var(--paper);
  }
  .card {
    position: relative;
    width: 1200px;
    height: 911px;
    font-family: "Crimson Text", Georgia, serif;
  }
  .guides {
    position: absolute;
    inset: 0;
    pointer-events: none;
  }
  .back-panel {
    position: absolute;
    left: 0;
    top: 0;
    width: 597px;
    height: 911px;
  }
  .brand {
    position: absolute;
    left: 0;
    top: 660px;
    width: 630px;
    display: flex;
    align-items: center;
    justify-content: center;
    gap: 14px;
  }
  .brand-dot {
    width: 20px;
    height: 20px;
    border-radius: 50%;
    background: var(--brand-blue);
  }
  .brand-name {
    font-size: 54px;
    font-weight: 600;
    color: var(--brand-blue);
    letter-spacing: 4px;
    line-height: 1;
  }
  .contact {
    position: absolute;
    left: 0;
    top: 772px;
    width: 614px;
    text-align: center;
    font-size: 17px;
    font-weight: 600;
    font-style: normal;
    line-height: 21px;
    color: var(--ink);
  }
  .front-panel {
    position: absolute;
    left: 598px;
    top: 0;
    width: 602px;
    height: 911px;
  }
  .cover-scene {
    position: absolute;
    left: 0;
    top: 0;
    width: 602px;
    height: 400px;
    background: linear-gradient(180deg,
      var(--forest-dark) 0%,
      var(--forest-mid) 30%,
      var(--snow-shade) 55%,
      var(--snow) 78%,
      var(--paper) 100%);
  }
  .greeting {
    position: absolute;
    left: 0;
    top: 352px;
    width: 616px;
    text-align: center;
    font-size: 34px;
    font-style: italic;
    color: var(--quote-blue);
    line-height: 1;
  }
  .blessing {
    position: absolute;
    left: 0;
    top: 418px;
    width: 616px;
    text-align: center;
    color: var(--quote-blue);
    font-size: 23.5px;
    line-height: 32.6px;
  }
  .blessing p { text-transform: uppercase; }
  .attribution { margin-top: 31px; }
</style>
</head>
<body>
<main class="card">
  <svg class="guides" width="1200" height="911" viewBox="0 0 1200 911" aria-hidden="true">
    <path d="M16 16 H578 Q590 16 590 28 V883 Q590 895 578 895 H16 Z" fill="none" stroke="var(--bleed-line)" stroke-width="1"/>
    <path d="M597 1 H1176 Q1190 1 1190 15 V896 Q1190 910 1176 910 H597 Z" fill="none" stroke="var(--trim-line)" stroke-width="1.2"/>
  </svg>

  <section class="back-panel">
    <div class="brand">
      <span class="brand-dot"></span>
      <span class="brand-name">QKRP</span>
    </div>
    <address class="contact">
      QKRP, LLC<br>
      418 E 3rd Street, Suite 102<br>
      Harlow, MD 21890, 800-555-0147<br>
      qkrpstudio.com
    </address>
  </section>

  <section class="front-panel">
    <div class="cover-scene" role="img" aria-label="Photo of a snow-covered red cabin among bare winter trees, fading into white snow"></div>
    <h1 class="greeting">Seasons Greetings</h1>
    <blockquote class="blessing">
      <p>We call upon the waters<br>
      that rim the earth,<br>
      horizon to horizon,<br>
      that flow in our rivers<br>
      and streams,<br>
      that fall upon our<br>
      gardens and fields,<br>
      and we ask that they teach us<br>
      and show us the way.</p>
      <p class="attribution">— Chinook Blessing Litany</p>
    </blockquote>
  </section>
</main>
</body>
</html>
```